WP website design (Dorlen Group)

We need a wordpress design for an established auction and real estate company based in Kansas. The winning design will incorporate a professional color scheme with company logo in a clean layout with specified widgets. The design needs to consider that this will be developed on a responsive theme. Colors are blue and gray, with perhaps black or other as an accent/highlight color.

Must Have:
- Navigation:
1) Home 2) Auctions 3) Real Estate Listings 4) Rentals 5) Our Team 6) Services 7) Past Auctions 8) Testimonials 9) Contact Us

Page will have large slideshow, please use either image provided as the initial slide. Homepage will have auctions - as at http://brindlebidhouse.com/upcoming-auctions/. Home page will also have 2 calls to action: "NOTIFY ME OF UPCOMING AUCTIONS" (newsletter signup), and "I AM READY TO SELL. PLEASE CONTACT ME FOR A FREE CONSULTATION." with an email button.

Footer will have smaller company logo, credit card logo, and attached association logos and this contact info:
.(555) 318-7061: OFFICE
(555) 318-7095: FAX
dgroup@vrbx.com: email
Address: 718 N. Elm Ave., Johnson KS
Mailing Address: PO Box 927, Johnson, KS

Widgets:
1) email sign up 2) Social media (twitter, FB, linked-in, pinterest) 3) Mortgage calculator 4) testimonials blog

Nice to Have:
- demonstrate the drop-down menu styling, e.g. under Auctions
Auction Calendar
4 Key Auction Methods
Auction Benefits

Industry/Entity Type

Real Estate

Font styles to use
Sans Serif

Colors

Designer to choose colors to be used in the design.

Requirements
Must have
• - Navigation:

.(555) 318-7061: OFFICE
(555) 318-7095: FAX
dgroup@vrbx.com: email

Widgets:
Nice to have
• Nice to Have:
Auction Calendar
4 Key Auction Methods
Auction Benefits

```html
<!DOCTYPE html>
<html lang="en">
<head>
<meta charset="utf-8">
<title>Dorlen Group – Auctions &amp; Real Estate</title>
<link href="https://fonts.googleapis.com/css2?family=Open+Sans:wght@400;600&display=swap" rel="stylesheet">
<style>
:root{
  --blue:#0a0aa8;
  --blue-dark:#00008a;
  --red:#d10410;
  --orange:#f0a81a;
  --ink:#222;
  --text:#444;
  --panel:#ececec;
  --footer:#2b2b2b;
  --footer-text:#bdbdbd;
}
*{margin:0;padding:0;box-sizing:border-box}
html,body{width:812px;height:1200px;overflow:hidden;background:#fff}
body{position:relative;font-family:"Open Sans",Arial,sans-serif;color:var(--text)}
.abs{position:absolute}

/* header */
.brand{left:116px;top:30px;display:flex;align-items:center;gap:6px;font-size:20px;color:var(--blue);font-weight:400}
.brand-mark{width:12px;height:12px;background:var(--blue)}
.search{left:564px;top:29px;width:126px;height:26px;border:1px solid #bbb;border-radius:3px;font-size:7px;color:#999;padding:8px 7px}
.search svg{position:absolute;right:7px;top:6px}

/* nav */
.nav{left:0;top:83px;width:812px;height:32px;background:var(--blue)}
.nav a{position:absolute;top:11px;font-size:8px;color:#fff;text-decoration:none}

/* hero */
.hero{left:0;top:115px;width:812px;height:360px;background:linear-gradient(180deg,#b8b7c2 0%,#8e8a9a 28%,#4b5640 31%,#2f4224 60%,#26391d 100%)}
.slide-arrow{width:24px;height:24px;border-radius:50%;background:#eee;border:3px solid rgba(0,0,0,.35);top:283px}

/* mortgage calculator */
.calc{left:122px;top:339px;width:172px;height:249px;background:var(--panel)}
.calc-head{height:30px;background:var(--blue);color:#fff;font-size:11.5px;padding:8px 11px}
.calc label{position:absolute;left:15px;font-size:7px;color:#555}
.calc .field{position:absolute;left:104px;width:56px;height:22px;background:#fafafa;border:1px solid #ccc;border-radius:2px}
.calc-btn{position:absolute;left:59px;top:210px;width:70px;height:24px;background:var(--red);color:#fff;font-size:11px;text-align:center;line-height:24px;border-radius:2px}

/* calls to action */
.cta{top:491px;width:184px;height:94px;background:var(--red);border:2px solid #f1d4d4;color:#fff;text-align:center}
.cta-notify{left:307px}
.cta-notify h3{font-weight:400;font-size:14px;line-height:18.5px;margin-top:8px;letter-spacing:.3px}
.email-row{position:absolute;left:11px;top:53px;width:160px;height:30px;display:flex}
.email-row .input{flex:1;background:#fff;color:#333;font-size:7px;text-align:left;padding:10px 8px}
.email-row .go{width:50px;background:var(--orange);font-size:10px;line-height:30px}
.cta-sell{left:504px}
.cta-sell p{font-size:10px;line-height:18.5px;margin-top:6px;padding:0 10px}
.mail-btn{position:absolute;left:81px;top:62px;width:22px;height:22px;border-radius:50%;background:#fff}

/* welcome */
.welcome-img{left:122px;top:616px;width:171px;height:141px;background:linear-gradient(135deg,#7b8a5c 0%,#b47d78 45%,#4a4a42 100%)}
.welcome{left:310px;top:612px;width:380px}
h2{font-weight:400;font-size:14px;color:var(--ink)}
.welcome p{font-size:6.9px;line-height:12.8px;text-align:justify;margin-top:7px}

/* testimonials */
.t-head{left:122px;top:773px}
.t-card{top:802px;width:181px}
.t-card .photo{height:108px;background:linear-gradient(135deg,#d9dde2,#8e9aa8)}
.t-card h4{font-weight:400;font-size:9px;color:var(--ink);margin-top:12px}
.t-card p{font-size:6.5px;line-height:12.8px;margin-top:10px}

/* footer */
.footer{left:0;top:1010px;width:812px;height:190px;background:var(--footer);color:var(--footer-text)}
.f-title{font-size:10px;color:#c8c8c8;top:18px}
.f-item{left:145px;font-size:8px;display:flex;align-items:center}
.f-icon{position:absolute;left:122px}
.cards{left:274px;top:30px;width:156px;height:36px;background:#fff;border-radius:2px;padding:5px;display:flex;gap:3px}
.cards span{flex:1;border:1px solid #999}
.badges{left:274px;top:75px;width:101px;height:50px;background:#fff;border-radius:2px;padding:8px;display:flex;gap:6px}
.badges span{flex:1;background:#dde}
.benefit-img{left:453px;top:33px;width:86px;height:80px;background:linear-gradient(180deg,#c9ccd2 0%,#b3aea3 50%,#4f6a34 70%,#3c5727 100%)}
.benefit{left:552px;top:34px;width:138px;font-size:8px;line-height:12.8px;color:#ddd;text-align:justify}
.benefit p{margin-bottom:3px}
.f-rule{left:122px;top:150px;width:568px;height:1px;background:#3c3c3c}
.f-brand{left:128px;top:164px;font-size:10px;color:#333;display:flex;align-items:center;gap:4px}
.f-brand i{width:7px;height:7px;background:#333}
.copy{left:214px;top:166px;font-size:6.5px;color:#999}
.social{top:165px;width:13px;height:13px;border-radius:50%}
</style>
</head>
<body>

<header>
  <div class="abs brand"><span class="brand-mark"></span>Dorlen Group</div>
  <div class="abs search">Search
    <svg width="12" height="12" viewBox="0 0 12 12"><circle cx="5" cy="5" r="3.6" fill="none" stroke="#2b3d8c" stroke-width="1.6"/><line x1="7.6" y1="7.6" x2="11" y2="11" stroke="#2b3d8c" stroke-width="2"/></svg>
  </div>
</header>

<nav class="abs nav">
  <a style="left:122px">Home</a>
  <a style="left:170px">Auctions</a>
  <a style="left:229px">Real Estate Listings</a>
  <a style="left:327px">Rentals</a>
  <a style="left:381px">Our Team</a>
  <a style="left:445px">Services</a>
  <a style="left:502px">Past Auctions</a>
  <a style="left:577px">Testimonials</a>
  <a style="left:648px">Contact Us</a>
</nav>

<section class="abs hero" role="img" aria-label="Slideshow photo: a rancher in a hat looking over a green field with power lines at dusk"></section>
<div class="abs slide-arrow" style="left:62px"><svg width="18" height="18" viewBox="0 0 18 18"><path d="M10.5 5 6.5 9l4 4" fill="none" stroke="#555" stroke-width="1.6"/></svg></div>
<div class="abs slide-arrow" style="left:729px"><svg width="18" height="18" viewBox="0 0 18 18"><path d="M7.5 5l4 4-4 4" fill="none" stroke="#555" stroke-width="1.6"/></svg></div>

<aside class="abs calc">
  <div class="calc-head">Mortgage Calculator</div>
  <label style="top:51px">Periodic Payments *</label><span class="field" style="top:45px"></span>
  <label style="top:82px">Interest Rate *</label><span class="field" style="top:76px"></span>
  <label style="top:113px">Payments Per Year *</label><span class="field" style="top:107px"></span>
  <label style="top:144px">Loan Amount *</label><span class="field" style="top:138px"></span>
  <label style="top:175px">Number Of Payments *</label><span class="field" style="top:169px"></span>
  <div class="calc-btn">Calculator</div>
</aside>

<div class="abs cta cta-notify">
  <h3>NOTIFY ME OF<br>UPCOMING AUCTIONS</h3>
  <div class="email-row"><span class="input">Enter Email</span><span class="go">Sign Up</span></div>
</div>
<div class="abs cta cta-sell">
  <p>I AM READY TO SELL. PLEASE CONTACT ME FOR A FREE CONSULTATION.</p>
  <span class="mail-btn"><svg width="22" height="22" viewBox="0 0 22 22"><rect x="5" y="7" width="12" height="8" fill="none" stroke="#111" stroke-width="1.4"/><path d="M5 7l6 5 6-5M5 15l4.5-4M17 15l-4.5-4" fill="none" stroke="#111" stroke-width="1.2"/></svg></span>
</div>

<div class="abs welcome-img" role="img" aria-label="Photo of a classic pink convertible car parked on grass"></div>
<section class="abs welcome">
  <h2>Welcome To Dorlen Group</h2>
  <p>Lorem ipsum dolor sit amet, consectetur adipiscing elit. Etiam dictum auctor interdum. Aenean egestas vehicula purus in euismod. Quisque gravida commodo velit, eget porta leo sagittis vel. Lorem ipsum dolor sit amet, consectetur adipiscing elit. Etiam dictum auctor interdum. Aenean egestas vehicula purus in euismod. Quisque gravida commodo velit, eget porta leo sagittis vel. Lorem ipsum dolor sit amet, consectetur adipiscing elit. Etiam dictum auctor interdum. Aenean egestas vehicula purus in euismod. Quisque gravida commodo velit, eget porta leo sagittis vel. Lorem ipsum dolor sit amet,</p>
  <p>Etiam dictum auctor interdum. Aenean egestas vehicula purus in euismod. Quisque gravida commodo velit, eget porta leo sagittis vel. Lorem ipsum dolor sit amet, consectetur adipiscing elit. Etiam dictum auctor interdum. Aenean egestas vehicula purus in euismod.</p>
</section>

<h2 class="abs t-head">Testimonials</h2>
<article class="abs t-card" style="left:122px">
  <div class="photo" role="img" aria-label="Photo of an agent reviewing papers with a client at a desk"></div>
  <h4>Donec sodales sagittis magna sed</h4>
  <p>Lorem ipsum dolor sit amet, consectetur adipiscing elit. Sed blandit massa vel mauris sollicitudin dignissim. Phasellus ultrices tellus eget ipsum ornare molestie scelerisque eros dignissim</p>
</article>
<article class="abs t-card" style="left:315px">
  <div class="photo" role="img" aria-label="Photo of a team meeting around a table"></div>
  <h4>Donec sodales sagittis magna sed</h4>
  <p>Lorem ipsum dolor sit amet, consectetur adipiscing elit. Sed blandit massa vel mauris sollicitudin dignissim. Phasellus ultrices tellus eget ipsum ornare molestie scelerisque eros dignissim</p>
</article>
<article class="abs t-card" style="left:509px">
  <div class="photo" role="img" aria-label="Photo of two colleagues discussing at a laptop"></div>
  <h4>Donec sodales sagittis magna sed</h4>
  <p>Lorem ipsum dolor sit amet, consectetur adipiscing elit. Sed blandit massa vel mauris sollicitudin dignissim. Phasellus ultrices tellus eget ipsum ornare molestie scelerisque eros dignissim</p>
</article>

<footer class="abs footer">
  <div class="abs f-title" style="left:122px">ADDRESS</div>
  <svg class="f-icon" style="top:38px" width="10" height="16" viewBox="0 0 10 16"><path d="M5 0a5 5 0 0 0-5 5c0 4 5 11 5 11s5-7 5-11a5 5 0 0 0-5-5z" fill="#111"/><circle cx="5" cy="5" r="1.8" fill="#2b2b2b"/></svg>
  <div class="abs f-item" style="top:39px">718 N. Elm Ave., Johnson KS</div>
  <svg class="f-icon" style="top:63px" width="10" height="17" viewBox="0 0 10 17"><rect x="0.5" y="0.5" width="9" height="16" rx="1.5" fill="#111" stroke="#555"/><rect x="2" y="3" width="6" height="9" fill="#333"/></svg>
  <div class="abs f-item" style="top:67px;left:147px">Call us: (555) 318-7061</div>
  <svg class="f-icon" style="top:96px" width="14" height="10" viewBox="0 0 14 10"><rect width="14" height="10" fill="#111"/><path d="M0 0l7 5 7-5" fill="none" stroke="#555"/></svg>
  <div class="abs f-item" style="top:95px;left:147px">dgroup@vrbx.com</div>

  <div class="abs cards"><span></span><span></span><span></span></div>
  <div class="abs badges"><span></span><span></span></div>

  <div class="abs f-title" style="left:453px">AUCTION BENEFITS</div>
  <div class="abs benefit-img" role="img" aria-label="Photo of a single-story ranch house with a lawn"></div>
  <div class="abs benefit">
    <p>Beautiful Yard, Nice Home!</p>
    <p>Sales Price: $80,000</p>
    <p>Double Car Garage, Sprinkler System, Fence Buyer Concessions: $2,500 Exterior Improvement Allowance</p>
  </div>

  <div class="abs f-rule"></div>
  <div class="abs f-brand"><i></i>Dorlen Group</div>
  <div class="abs copy">Copyright © 2014 | Privacy Policy</div>
  <span class="abs social" style="left:624px;background:#3b5fae"></span>
  <span class="abs social" style="left:642px;background:#2c8fd6"></span>
  <span class="abs social" style="left:660px;background:#1f6fb0"></span>
  <span class="abs social" style="left:678px;background:#cc2020"></span>
</footer>

</body>
</html>
```